Infographic for Yoga Weight Loss in 10 Steps

I need a clever, striking infographic

8 1/2 by 11 or A4

High Resolution

I already put the ten main topics with "excerpts" below, so what is below is what goes in

must say discretely [url removed, login to view] somewhere

```html
<!DOCTYPE html>
<html lang="en">
<head>
<meta charset="utf-8">
<title>11 Steps of Yoga for Weight Loss</title>
<link rel="stylesheet" href="https://fonts.googleapis.com/css2?family=Alfa+Slab+One&family=Arimo:ital,wght@0,400;0,700;1,700&display=swap">
<style>
  :root {
    --ink: #1f1f1f;
    --purple: #9a2c9c;
    --icon-fill: #efdcf0;
    --paper: #ffffff;
  }
  * { margin: 0; padding: 0; box-sizing: border-box; }
  html, body { width: 927px; height: 1200px; overflow: hidden; background: var(--paper); }
  .sheet { position: relative; width: 927px; height: 1200px; font-family: "Arimo", Arial, sans-serif; color: var(--ink); }

  .title { position: absolute; left: 22px; top: 14px; width: 275px; font-family: "Alfa Slab One", serif; line-height: 1.02; }
  .title-line { display: block; font-size: 52px; letter-spacing: 1px; }
  .title-mid { font-size: 30px; }
  .title-mid .accent { font-size: 50px; color: var(--purple); }
  .byline { display: block; margin-top: 6px; font-family: "Arimo", Arial, sans-serif; font-size: 12px; color: var(--purple); padding-left: 70px; }

  .icon { position: absolute; width: 66px; height: 66px; }

  .step { position: absolute; width: 282px; }
  .step h2 { font-family: "Alfa Slab One", serif; font-weight: 400; font-size: 21px; line-height: 1.05; color: var(--purple); text-transform: uppercase; margin-bottom: 3px; }
  .step h2 .num { color: var(--ink); margin-right: 6px; }
  .step p, .step li { font-size: 14.6px; line-height: 18.3px; }
  .step .em { font-weight: 700; font-style: italic; color: var(--purple); }
  .step ul { list-style: none; }
  .step li { padding-left: 14px; position: relative; }
  .step li::before { content: "•"; position: absolute; left: 2px; }
</style>
</head>
<body>
<div class="sheet">

  <h1 class="title">
    <span class="title-line">11 STEPS</span>
    <span class="title-line title-mid">of <span class="accent">YOGA</span> for</span>
    <span class="title-line">WEIGHT</span>
    <span class="title-line">LOSS</span>
    <span class="byline">by LunaPathYoga.com</span>
  </h1>

  <!-- icons -->
  <svg class="icon" style="left:409px;top:12px" viewBox="0 0 66 66" role="img" aria-label="Yoga pose figure: seated meditation"><circle cx="33" cy="33" r="30" fill="var(--icon-fill)" stroke="var(--purple)" stroke-width="3"/></svg>
  <svg class="icon" style="left:704px;top:8px" viewBox="0 0 66 66" role="img" aria-label="Yoga pose figure: boat pose"><circle cx="33" cy="33" r="30" fill="var(--icon-fill)" stroke="var(--purple)" stroke-width="3"/></svg>
  <svg class="icon" style="left:127px;top:292px" viewBox="0 0 66 66" role="img" aria-label="Yoga pose figure: cobra pose"><circle cx="33" cy="33" r="30" fill="var(--icon-fill)" stroke="var(--purple)" stroke-width="3"/></svg>
  <svg class="icon" style="left:409px;top:292px" viewBox="0 0 66 66" role="img" aria-label="Yoga pose figure: upward dog"><circle cx="33" cy="33" r="30" fill="var(--icon-fill)" stroke="var(--purple)" stroke-width="3"/></svg>
  <svg class="icon" style="left:704px;top:292px" viewBox="0 0 66 66" role="img" aria-label="Yoga pose figure: dancer pose"><circle cx="33" cy="33" r="30" fill="var(--icon-fill)" stroke="var(--purple)" stroke-width="3"/></svg>
  <svg class="icon" style="left:127px;top:576px" viewBox="0 0 66 66" role="img" aria-label="Yoga pose figure: wheel pose"><circle cx="33" cy="33" r="30" fill="var(--icon-fill)" stroke="var(--purple)" stroke-width="3"/></svg>
  <svg class="icon" style="left:409px;top:576px" viewBox="0 0 66 66" role="img" aria-label="Yoga pose figure: standing pose"><circle cx="33" cy="33" r="30" fill="var(--icon-fill)" stroke="var(--purple)" stroke-width="3"/></svg>
  <svg class="icon" style="left:704px;top:576px" viewBox="0 0 66 66" role="img" aria-label="Yoga pose figure: sphinx pose"><circle cx="33" cy="33" r="30" fill="var(--icon-fill)" stroke="var(--purple)" stroke-width="3"/></svg>
  <svg class="icon" style="left:127px;top:874px" viewBox="0 0 66 66" role="img" aria-label="Yoga pose figure: plough pose"><circle cx="33" cy="33" r="30" fill="var(--icon-fill)" stroke="var(--purple)" stroke-width="3"/></svg>
  <svg class="icon" style="left:409px;top:874px" viewBox="0 0 66 66" role="img" aria-label="Yoga pose figure: pigeon pose"><circle cx="33" cy="33" r="30" fill="var(--icon-fill)" stroke="var(--purple)" stroke-width="3"/></svg>
  <svg class="icon" style="left:704px;top:874px" viewBox="0 0 66 66" role="img" aria-label="Yoga pose figure: warrior pose"><circle cx="33" cy="33" r="30" fill="var(--icon-fill)" stroke="var(--purple)" stroke-width="3"/></svg>

  <section class="step" style="left:320px;top:86px;width:262px">
    <h2><span class="num">1.</span>Change the word</h2>
    <p>When you “loose something“ you have to…FIND IT!!! Right?! Instead let’s think of it this way: I AM READY TO “RELEASE” WEIGH. <span class="em">“Releasing” is for something we are ready to let go of… For good.</span> You may think it is simple or silly, but it’s not. The forces of pre-programming in our mind (known as samskaras in yoga) are very strong.</p>
  </section>

  <section class="step" style="left:615px;top:80px;width:292px">
    <h2><span class="num">2.</span>Practicing yoga daily informs the breathing and body</h2>
    <p>When you practice yoga intelligently, meaning that BREATHING is the priority, body begins to work in a more efficient way. <span class="em">THE BEST SHORTCUT TO RELEASE WEIGHT IS TO APPROACH IT FROM ALL ANGLES.</span></p>
  </section>

  <section class="step" style="left:22px;top:366px;width:272px">
    <h2><span class="num">3.</span>Not stealing and not harming helps</h2>
    <p>Not picking up a fight at work is helpful. It sounds obvious but the first two limbs of yoga, abstentions and observances, DO come as a surprise. We begin to question: <span class="em">What does it mean to maintain “contentment”, “cleanliness”, “an attitude of surrender”, to be “grateful”?</span></p>
  </section>

  <section class="step" style="left:320px;top:366px;width:268px">
    <h2><span class="num">4.</span>Things we let go</h2>
    <p>The practice sets the odds in our favor. No food transformation can happen drastically and immediately. A meat eater cannot just leave meat, it won’t work. <span class="em">Trying to change it all at once because “someone said so” is not real.</span> There are levels. It begins to happen naturally. One day at the time.</p>
  </section>

  <section class="step" style="left:615px;top:366px;width:292px">
    <h2><span class="num">5.</span>We get out of the ‘fat’ blind spot</h2>
    <p>The “fat free” craze of the 90s got to us in a bad way. <span class="em">The brain NEEDS fats, of the good kind, which are:</span></p>
    <ul>
      <li>Olive oil for salads</li>
      <li>Ghee or regular butter BUT from cows that eat grass (not genetically modified corn)</li>
      <li>Coconut Oil (good quality) for frying</li>
    </ul>
  </section>

  <section class="step" style="left:22px;top:652px;width:272px">
    <h2><span class="num">6.</span>Our thinking becomes clear</h2>
    <p>We become idea machines. Writing ten ideas has these three specific effects:</p>
    <ul>
      <li>Keeps the brain sharp</li>
      <li>Stops the monkey mind</li>
      <li>Transforms your life for the better every six months</li>
    </ul>
    <p class="em">Magic happens when we play with ideas regularly.</p>
  </section>

  <section class="step" style="left:320px;top:652px;width:262px">
    <h2><span class="num">7.</span>Breathing leads to weight release: Idea X talk says</h2>
    <p>Daniel Ashford in his IDEAx talk asks a simple question: When you release weigh... WHERE does it go?! The science and math show that <span class="em">weight is released on THE EXHALE...</span> Try this simple exercise: sit down comfortably and breathe in for 4 counts and exhale for 8.</p>
  </section>

  <section class="step" style="left:615px;top:652px;width:292px">
    <h2><span class="num">8.</span>Declutter your house equals release weight</h2>
    <p>I never thought that emptying my house would lead to such an emotional “dump”. <span class="em">As we let go of everything externally that no longer serves us, we ALSO let go of what no longer serves us internally,</span> including what we put into our bodies.</p>
  </section>

  <section class="step" style="left:22px;top:953px;width:274px">
    <h2><span class="num">9.</span>Releasing crappy people</h2>
    <p>The people who drag us down, who tell us we are not good enough, ….They’ve got to go! You KNOW who those people are. <span class="em">Having people who drag you down around is like enabling a vampire to suck from your neck,</span> and empty you of vibrant red, life-filled blood, which you need…</p>
  </section>

  <section class="step" style="left:320px;top:953px;width:264px">
    <h2><span class="num">10.</span>We choose ourselves</h2>
    <p>We shift “outer reference” to “inner reference“. And by that I mean we stop worrying about what others are thinking and we get busy with how interesting and good our life gets. <span class="em">We refer to ourselves, we know when we did good work and we know when we missed the mark…</span></p>
  </section>

  <section class="step" style="left:615px;top:953px;width:292px">
    <h2><span class="num">11.</span>We continue the daily practice and we are at our perfect weight</h2>
    <p>The real science laboratory is now a days in our bodies. We can read all we want but in the end it is you who has to find and use what works for you. <span class="em">It is only you that can choose yourself.</span></p>
  </section>

</div>
</body>
</html>
```